UI/ UX Design for ERP Software

We need a new UX/UI interface for a ERP software for property managers. Our CMMS / ERP solution is made based on responsive design technologies and is coded in PHP.
The overall UX to be similar to Zel Kavo - easy navigation, intuitive menus.

Industry/Entity Type

Property Management

Number of Pages Required

5+ page

Requirements
Must have
• Round dock buttons
Consistent icons across the application
Enough Spacing between buttons/icons/ menu
Consistent Font
Nice to have
• We would like the UX to allow the users to use the application without /minimum training.
Should not have
• we don't want anything that is classic with respect to UX

```html
<!DOCTYPE html>
<html lang="en">
<head>
<meta charset="utf-8">
<title>Keystead – Properties list</title>
<link href="https://fonts.googleapis.com/css2?family=Nunito+Sans:wght@400;600;700;800&display=swap" rel="stylesheet">
<style>
:root{
  --bg:#252630;
  --card:#30323f;
  --chip:#363846;
  --text:#ffffff;
  --muted:#b4bfd6;
  --blue:#1390ff;
  --blue-dark:#1468e6;
  --blue-light:#cfe5ff;
  --cyan:#14b4ff;
  --cyan-light:#a6e3ff;
  --orange:#f2703d;
  --peach:#f7d1c3;
  --yellow:#fdb93d;
  --dock:#1d1e26;
}
*{box-sizing:border-box;margin:0;padding:0}
html,body{width:1200px;height:1200px;overflow:hidden}
body{background:var(--bg);font-family:"Nunito Sans",sans-serif;color:var(--text)}
.app{position:relative;width:1200px;height:1200px}
.abs{position:absolute}

.brand{left:49px;top:100px;display:flex;align-items:center;gap:8px;font-weight:800;font-size:19px}
.brand-mark{width:16px;height:16px;border-radius:50%;background:var(--text)}
.theme-toggle{left:860px;top:98px;width:71px;height:28px;border-radius:14px;background:#2c2e3a;display:flex;align-items:center;justify-content:space-between;padding:0 10px}
.welcome{left:948px;top:102px;font-size:14px;font-weight:600}
.welcome b{font-weight:800}
.avatar{left:1112px;top:89px;width:46px;height:46px;border-radius:50%;background:linear-gradient(135deg,#8a6a58,#3c3f4c)}

.page-title{left:43px;top:140px;display:flex;align-items:center;gap:14px;font-size:21px;font-weight:800}

.tabs{left:43px;top:202px;display:flex;gap:7px}
.tab{width:124px;height:38px;border-radius:6px;background:var(--chip);font-size:11px;font-weight:700;display:flex;align-items:center;justify-content:center}

.action{top:263px;height:54px;border-radius:4px;display:flex;align-items:center;justify-content:center;gap:8px;font-size:13px}
.action-primary{left:43px;width:186px;background:var(--blue);font-weight:800;box-shadow:0 6px 18px rgba(19,144,255,.3)}
.action-secondary{left:256px;width:210px;background:#fff;color:#1d1e26;font-weight:600}

.stat{width:160px;border-radius:8px;background:var(--card);padding:18px 12px 0;text-align:center}
.stat h3{font-size:11px;font-weight:800;line-height:1.35}
.stat svg{display:block;margin:18px auto 0}
.legend{list-style:none;text-align:left;margin-top:22px;font-size:11px;font-weight:700}
.legend li{display:flex;align-items:center;gap:10px;line-height:17px}
.legend .dim{color:var(--muted)}
.dot{width:6px;height:6px;border-radius:50%}

.panel{left:221px;width:769px;height:156px;border-radius:8px;background:var(--card)}
.panel h2{position:absolute;left:17px;top:20px;font-size:17px;font-weight:800}
.grid{position:absolute;left:30px;top:57px;width:720px;border-collapse:collapse}
.grid th{font-size:13px;font-weight:800;text-align:left;padding-bottom:10px}
.grid td{font-size:12.5px;color:var(--muted);font-weight:600;height:28px}
.c1{width:108px}.c2{width:204px}.c3{width:127px}.c4{width:146px}

.dock{left:504px;top:1039px;width:190px;height:75px;border-radius:14px;background:var(--dock);display:flex;align-items:center;justify-content:center;gap:40px}
.dock-btn{width:50px;height:50px;border-radius:12px;display:flex;align-items:center;justify-content:center}
.dock-home{background:linear-gradient(160deg,#1fa8ff,#0a78f0)}
.dock-apps{background:linear-gradient(160deg,#ff8a3a,#f2622d)}
</style>
</head>
<body>
<main class="app">
  <div class="abs brand"><span class="brand-mark"></span>Keystead</div>
  <div class="abs theme-toggle">
    <svg width="16" height="16" viewBox="0 0 16 16"><circle cx="8" cy="8" r="7" fill="none" stroke="#4a4d5c" stroke-width="2"/></svg>
    <svg width="18" height="18" viewBox="0 0 18 18"><path d="M12 2a7 7 0 1 0 4 11A6 6 0 0 1 12 2z" fill="none" stroke="#fff" stroke-width="1.6"/></svg>
  </div>
  <div class="abs welcome">Welcome, <b>Mira Dallen</b></div>
  <div class="abs avatar" role="img" aria-label="User profile photo"></div>

  <h1 class="abs page-title">
    <svg width="24" height="24" viewBox="0 0 24 24" fill="none" stroke="#fff" stroke-width="1.4"><rect x="3" y="3" width="10" height="18"/><rect x="13" y="9" width="8" height="12"/><path d="M6 7h4M6 10h4M6 13h4M16 13h2M16 16h2M7 21v-4h2v4"/></svg>
    Properties list
  </h1>

  <nav class="abs tabs">
    <div class="tab">Prime tower</div><div class="tab">Prime tower</div><div class="tab">Prime tower</div><div class="tab">Prime tower</div><div class="tab">Prime tower</div><div class="tab">Prime tower</div><div class="tab">Prime tower</div>
  </nav>

  <div class="abs action action-primary">
    <svg width="16" height="16" viewBox="0 0 16 16" fill="none" stroke="#fff" stroke-width="1.5"><rect x="2" y="3" width="12" height="12" rx="1.5"/><path d="M5 1.5v3M11 1.5v3"/></svg>
    Request / orders
  </div>
  <div class="abs action action-secondary">
    <svg width="15" height="15" viewBox="0 0 16 16" fill="none" stroke="#1d1e26" stroke-width="1.4"><rect x="1.5" y="3" width="13" height="11.5" rx="1"/><path d="M1.5 6.5h13M5 1.5v3M11 1.5v3"/></svg>
    Maintenance calendar
  </div>

  <section class="abs stat" style="left:43px;top:342px;height:186px">
    <h3>Tenant request by user</h3>
    <svg width="72" height="72" viewBox="0 0 80 80"><circle cx="40" cy="40" r="40" fill="var(--blue-light)"/><path d="M40 40L40 0A40 40 0 0 1 68.3 68.3Z" fill="var(--blue-dark)"/></svg>
    <ul class="legend"><li class="dim"><span class="dot" style="background:var(--blue-light)"></span>No complete (100)</li><li><span class="dot" style="background:var(--blue-dark)"></span>Completed (65)</li></ul>
  </section>
  <section class="abs stat" style="left:43px;top:549px;height:186px">
    <h3>Maintenance by user</h3>
    <svg width="72" height="72" viewBox="0 0 80 80"><circle cx="40" cy="40" r="40" fill="var(--peach)"/><path d="M40 40L40 0A40 40 0 0 1 68.3 68.3Z" fill="var(--orange)"/></svg>
    <ul class="legend"><li class="dim"><span class="dot" style="background:var(--blue-light)"></span>No complete (100)</li><li><span class="dot" style="background:var(--orange)"></span>Completed (65)</li></ul>
  </section>

  <section class="abs panel" style="top:342px"><h2>Tenant request</h2>
    <table class="grid"><tr><th class="c1">Ticket ID</th><th class="c2">Subject</th><th class="c3">Date</th><th class="c4">Property</th><th>Tenant</th></tr>
    <tr><td>1232132323</td><td>Request for rent freeze</td><td>01/01/2021</td><td>Prime tower</td><td>Tara Velling</td></tr>
    <tr><td>1232132323</td><td>Bad neighboors</td><td>01/01/2021</td><td>Prime tower</td><td>Tara Velling</td></tr></table></section>
  <section class="abs panel" style="top:516px"><h2>Maintenance</h2>
    <table class="grid"><tr><th class="c1">Ticket ID</th><th class="c2">Subject</th><th class="c3">Date</th><th class="c4">Property</th><th>Tenant</th></tr>
    <tr><td>1232132323</td><td>Request for rent freeze</td><td>01/01/2021</td><td>Prime tower</td><td>Tara Velling</td></tr>
    <tr><td>1232132323</td><td>Bad neighboors</td><td>01/01/2021</td><td>Prime tower</td><td>Tara Velling</td></tr></table></section>
  <section class="abs panel" style="top:684px"><h2>Work orders</h2>
    <table class="grid"><tr><th class="c1">Ticket ID</th><th class="c2">Subject</th><th class="c3">Date</th><th class="c4">Property</th><th>Tenant</th></tr>
    <tr><td>1232132323</td><td>Request for rent freeze</td><td>01/01/2021</td><td>Prime tower</td><td>Tara Velling</td></tr>
    <tr><td>1232132323</td><td>Bad neighboors</td><td>01/01/2021</td><td>Prime tower</td><td>Tara Velling</td></tr></table></section>
  <section class="abs panel" style="top:852px"><h2>Purcharse orders</h2>
    <table class="grid"><tr><th class="c1">Ticket ID</th><th class="c2">Subject</th><th class="c3">Date</th><th class="c4">Property</th><th>Tenant</th></tr>
    <tr><td>1232132323</td><td>Request for rent freeze</td><td>01/01/2021</td><td>Prime tower</td><td>Tara Velling</td></tr>
    <tr><td>1232132323</td><td>Bad neighboors</td><td>01/01/2021</td><td>Prime tower</td><td>Tara Velling</td></tr></table></section>

  <section class="abs stat" style="left:1007px;top:342px;height:186px">
    <h3>Montly maintenance</h3>
    <svg width="72" height="72" viewBox="0 0 80 80"><circle cx="40" cy="40" r="40" fill="var(--cyan-light)"/><path d="M40 40L40 0A40 40 0 0 1 68.3 68.3Z" fill="var(--cyan)"/></svg>
    <ul class="legend"><li class="dim"><span class="dot" style="background:var(--cyan-light)"></span>No complete (100)</li><li><span class="dot" style="background:var(--cyan)"></span>Completed (65)</li></ul>
  </section>
  <section class="abs stat" style="left:1007px;top:548px;height:178px">
    <h3>Purcharse orders<br>this week</h3>
    <svg width="140" height="96" viewBox="0 0 140 96" style="margin-top:10px">
      <rect x="33" y="0" width="64" height="22" rx="4" fill="#fff"/>
      <path d="M61 22l4 6 4-6z" fill="#fff"/>
      <text x="65" y="15" text-anchor="middle" font-family="Nunito Sans,sans-serif" font-size="9" font-weight="700" fill="#1d1e26">8 orders</text>
      <path d="M0 86L12 76L20 78L36 54L46 66L56 52L66 64L78 58L100 30L140 86Z" fill="var(--yellow)"/>
      <circle cx="66" cy="50" r="6" fill="var(--orange)" stroke="var(--yellow)" stroke-width="3"/>
    </svg>
  </section>

  <nav class="abs dock">
    <div class="dock-btn dock-home"><svg width="22" height="22" viewBox="0 0 22 22"><path d="M3 10L11 3l8 7v9h-5v-5H8v5H3z" fill="#fff"/></svg></div>
    <div class="dock-btn dock-apps"><svg width="22" height="22" viewBox="0 0 22 22" fill="#fff"><circle cx="4" cy="4" r="2"/><circle cx="11" cy="4" r="2"/><circle cx="18" cy="4" r="2"/><circle cx="4" cy="11" r="2"/><circle cx="11" cy="11" r="2"/><circle cx="18" cy="11" r="2"/><circle cx="4" cy="18" r="2"/><circle cx="11" cy="18" r="2"/><circle cx="18" cy="18" r="2"/></svg></div>
  </nav>
</main>
</body>
</html>
```